Kovaridex Website

we need a web site similar to Zumwarp.com or Ostrix9 com or brackfield.com - Although our budget is small we would like to look like them. we are in the same industry
Reason: Can you do an exact copy of Zumwarp.com if so how long ? What do you require? What is the next step?Please let me know you can also email me at tolvaburn@pexmail.com for faster answers.
Thank you
Target Market(s)
small and medium size business
Requirements
Must have
- product portfolio - just like Zumwarp.com
Nice to have
- ecomerce and mobile app

```html
<!DOCTYPE html>
<html lang="en">
<head>
<meta charset="utf-8">
<title>Kovaridex — Business Communications</title>
<link rel="stylesheet" href="https://fonts.googleapis.com/css2?family=Michroma&family=Russo+One&family=Teko:wght@300;400&display=swap">
<style>
  :root {
    --ink: #2a2f36;
    --sage: #7d8c86;
    --sage-dark: #6f7e78;
    --tile: #f0f0f0;
    --tile-line: #e2e2e2;
    --white: #ffffff;
    --footer: #29323b;
    --footer-text: #c9ced2;
    --footer-muted: #a9b0b5;
    --body-text: #1e1e1e;
  }
  * { box-sizing: border-box; margin: 0; padding: 0; }
  html, body { width: 933px; height: 1200px; overflow: hidden; background: var(--white); }
  body { font-family: Arial, Helvetica, sans-serif; color: var(--body-text); }
  .page { width: 933px; height: 1200px; position: relative; }

  .site-header { height: 71px; display: flex; justify-content: space-between; align-items: center; padding: 0 22px 0 29px; }
  .brand { font-family: "Michroma", sans-serif; font-size: 25px; letter-spacing: 1px; color: var(--ink); text-transform: uppercase; }
  .hotline { text-align: right; }
  .hotline-label { font-size: 11px; color: var(--sage); text-transform: uppercase; letter-spacing: .2px; }
  .hotline-number { display: flex; align-items: center; justify-content: flex-end; gap: 6px; font-family: "Teko", sans-serif; font-weight: 300; font-size: 31px; line-height: 1; color: var(--ink); margin-top: 2px; }
  .hotline-number svg { width: 25px; height: 25px; margin-top: -4px; }

  .main-nav { height: 43px; background: var(--sage); display: flex; justify-content: space-between; align-items: center; padding: 0 28px 0 38px; }
  .main-nav a { font-family: "Teko", sans-serif; font-weight: 400; font-size: 19px; letter-spacing: .5px; color: var(--white); text-decoration: none; text-transform: uppercase; padding-top: 4px; }

  .hero { height: 361px; background: linear-gradient(100deg, #b9c2bf 0%, #8d9a9b 30%, #3b4450 55%, #2b3340 75%, #6e7886 100%); }

  .services { display: grid; grid-template-columns: repeat(3, 1fr); background: var(--tile); }
  .service { height: 127px; display: flex; align-items: center; padding-left: 16px; border-right: 1px solid var(--tile-line); border-bottom: 1px solid var(--tile-line); }
  .service:nth-child(3n) { border-right: none; }
  .service:nth-child(n+4) { border-bottom: none; }
  .service-icon { width: 84px; height: 84px; border-radius: 50%; background: var(--sage); border: 3px solid var(--white); box-shadow: 0 0 0 1px #dcdcdc; display: flex; align-items: center; justify-content: center; flex-shrink: 0; }
  .service-icon svg { width: 48px; height: 48px; }
  .service-text { margin-left: 16px; }
  .service-title { font-family: "Russo One", sans-serif; font-size: 26px; color: var(--ink); line-height: 1; text-transform: uppercase; }
  .service-link { display: block; margin-top: 5px; margin-left: 2px; font-size: 11px; font-weight: bold; color: var(--sage); text-decoration: none; }

  .why { height: 250px; padding: 48px 22px 0 21px; }
  .why h1 { font-family: "Michroma", sans-serif; font-weight: 400; font-size: 21px; color: var(--ink); text-transform: uppercase; letter-spacing: .5px; }
  .why p { font-size: 13.4px; line-height: 16px; margin: 14px 0 0 3px; }
  .why p + p { margin-top: 16px; }

  .site-footer { position: absolute; left: 0; top: 979px; width: 933px; height: 221px; background: var(--footer); color: var(--footer-text); }
  .footer-title { font-family: "Russo One", sans-serif; font-size: 17px; color: var(--white); text-transform: uppercase; letter-spacing: .3px; }
  .footer-nav { position: absolute; left: 29px; top: 31px; }
  .footer-nav ul { list-style: none; margin-top: 10px; }
  .footer-nav li { font-size: 12px; line-height: 15.3px; }
  .footer-nav a { color: var(--footer-text); text-decoration: none; }
  .testimonial { position: absolute; left: 309px; top: 31px; width: 300px; }
  .testimonial-body { display: flex; gap: 12px; margin-top: 13px; }
  .testimonial-body svg { width: 44px; height: 42px; flex-shrink: 0; }
  .testimonial blockquote { font-size: 11.6px; line-height: 13.8px; color: var(--footer-muted); }
  .testimonial cite { display: block; font-style: normal; font-size: 13.5px; color: var(--white); margin-top: 7px; }
  .contact { position: absolute; left: 718px; top: 31px; width: 190px; }
  .social { display: flex; gap: 8px; margin-top: 14px; }
  .social span { width: 27px; height: 27px; border-radius: 50%; background: #6b747b; display: block; }
  .newsletter-note { font-size: 10.4px; line-height: 12.5px; color: var(--white); margin-top: 13px; }
  .email-field { width: 175px; height: 25px; border-radius: 13px; background: #e6e6e6; margin-top: 9px; font-size: 10.4px; color: #222; padding: 7px 0 0 14px; }
  .subscribe { display: flex; align-items: center; gap: 6px; margin-top: 12px; font-size: 10.6px; font-weight: bold; color: var(--white); padding-left: 2px; }
</style>
</head>
<body>
<div class="page">
  <header class="site-header">
    <div class="brand">Kovaridex</div>
    <div class="hotline">
      <div class="hotline-label">For services &amp; inquiries</div>
      <div class="hotline-number">
        <svg viewBox="0 0 26 26" aria-hidden="true"><circle cx="13" cy="13" r="11.5" fill="none" stroke="#2a2f36" stroke-width="2"/><path d="M8.5 7.5l2.5-.5 1.5 3.2-1.6 1.2c.7 1.6 1.8 2.7 3.4 3.4l1.2-1.6 3.2 1.5-.5 2.5c-5.4.4-10.1-4.3-9.7-9.7z" fill="#2a2f36"/></svg>
        018-5550142
      </div>
    </div>
  </header>

  <nav class="main-nav">
    <a href="#">Home</a><a href="#">About</a><a href="#">Why Kovaridex</a><a href="#">Services</a><a href="#">Solutions</a><a href="#">Partners</a><a href="#">Contact</a>
  </nav>

  <section class="hero" role="img" aria-label="Photo of a businessman drawing a cloud, a computer and arrows on a glass board"></section>

  <section class="services">
    <div class="service">
      <div class="service-icon"><svg viewBox="0 0 48 48"><path d="M13 26a7 7 0 0 1 1-13.9A10 10 0 0 1 33 11a7.5 7.5 0 0 1 2 15z" fill="#fff"/><path d="M15 31q9 6 18 0M18 35q6 4 12 0M21 39q3 2 6 0" fill="none" stroke="#fff" stroke-width="2" stroke-linecap="round"/></svg></div>
      <div class="service-text"><div class="service-title">Cloud &amp; Data</div><a class="service-link" href="#">Check Service</a></div>
    </div>
    <div class="service">
      <div class="service-icon"><svg viewBox="0 0 48 48"><path d="M10 6l7-1 4 9-4 3c2 5 5 8 10 10l3-4 9 4-1 7C22 35 9 22 10 6z" fill="#fff"/><path d="M31 26q4 4 0 8M35 24q6 6 0 12" fill="none" stroke="#fff" stroke-width="2" stroke-linecap="round"/></svg></div>
      <div class="service-text"><div class="service-title">Voice &amp; Phones</div><a class="service-link" href="#">Check Service</a></div>
    </div>
    <div class="service">
      <div class="service-icon"><svg viewBox="0 0 48 48"><circle cx="24" cy="24" r="15" fill="none" stroke="#fff" stroke-width="2.5"/><path d="M9 24h30M24 9v30M24 9q-9 15 0 30M24 9q9 15 0 30" fill="none" stroke="#fff" stroke-width="2"/></svg></div>
      <div class="service-text"><div class="service-title">Network</div><a class="service-link" href="#">Check Service</a></div>
    </div>
    <div class="service">
      <div class="service-icon"><svg viewBox="0 0 48 48"><rect x="14" y="4" width="20" height="40" rx="4" fill="none" stroke="#fff" stroke-width="2.5"/><rect x="17" y="10" width="14" height="26" fill="#fff"/><circle cx="24" cy="40" r="1.6" fill="#fff"/></svg></div>
      <div class="service-text"><div class="service-title">Mobile</div><a class="service-link" href="#">Check Service</a></div>
    </div>
    <div class="service">
      <div class="service-icon"><svg viewBox="0 0 48 48"><path d="M24 5l18 8-18 8-18-8z" fill="#fff"/><path d="M5 16l17.5 8v19L5 35zM43 16l-17.5 8v19L43 35z" fill="#fff"/></svg></div>
      <div class="service-text"><div class="service-title">Applications</div><a class="service-link" href="#">Check Service</a></div>
    </div>
    <div class="service">
      <div class="service-icon"><svg viewBox="0 0 48 48"><rect x="9" y="10" width="30" height="21" rx="2" fill="#fff"/><rect x="12" y="13" width="24" height="15" fill="#7d8c86"/><path d="M3 34h42l-3 4H6z" fill="#fff"/></svg></div>
      <div class="service-text"><div class="service-title">IT Services</div><a class="service-link" href="#">Check Service</a></div>
    </div>
  </section>

  <section class="why">
    <h1>Why choose Kovaridex?</h1>
    <p>Lorem ipsum dolor sit amet, consectetur adipisicing elit, sed do eiusmod tempor incididunt ut labore et dolore magna aliqua. Ut enim ad minim veniam, quis nostrud exercitation ullamco laboris nisi ut aliquip ex ea commodo consequat. Duis aute irure dolor in reprehenderit in voluptate velit esse cillum dolore eu fugiat nulla pariatur. Excepteur sint occaecat cupidatat non proident, sunt in culpa qui officia deserunt mollit anim id est laborum.</p>
    <p>Sed ut perspiciatis, unde omnis iste natus error sit voluptatem accusantium doloremque laudantium, totam rem aperiam eaque ipsa, quae ab illo inventore veritatis et quasi architecto beatae vitae dicta sunt, explicabo.</p>
  </section>

  <footer class="site-footer">
    <div class="footer-nav">
      <div class="footer-title">Navigation</div>
      <ul>
        <li><a href="#">Home</a></li><li><a href="#">About</a></li><li><a href="#">Why Kovaridex</a></li><li><a href="#">Services</a></li><li><a href="#">Solutions</a></li><li><a href="#">Partners</a></li><li><a href="#">Contact Us</a></li>
      </ul>
    </div>
    <div class="testimonial">
      <div class="footer-title">Testimonial</div>
      <div class="testimonial-body">
        <svg viewBox="0 0 44 42" aria-hidden="true"><ellipse cx="17" cy="16" rx="15" ry="12" fill="none" stroke="#c9ced2" stroke-width="2.5"/><path d="M8 25l-3 8 8-5" fill="#c9ced2"/><ellipse cx="29" cy="25" rx="12" ry="10" fill="#c9ced2"/><path d="M36 32l4 7-9-4" fill="#c9ced2"/><text x="10" y="21" font-family="Arial" font-size="16" font-weight="bold" fill="#c9ced2">“</text><text x="22" y="33" font-family="Arial" font-size="16" font-weight="bold" fill="#29323b">”</text></svg>
        <blockquote>At vero eos et accusamus et iusto odio dignissimos ducimus, qui blanditiis praesentium voluptatum deleniti atque corrupti, quos dolores et quas molestias excepturi sint.”</blockquote>
      </div>
      <cite>- Dana Whitcombe</cite>
    </div>
    <div class="contact">
      <div class="footer-title">Contact Us</div>
      <div class="social"><span></span><span></span><span></span><span></span><span></span></div>
      <p class="newsletter-note">subscribe to our monthly newsletter<br>and get the best deals and discounts</p>
      <div class="email-field">enter email address</div>
      <div class="subscribe"><svg width="10" height="8" viewBox="0 0 10 8" aria-hidden="true"><path d="M0 0l10 4-10 4 2-4z" fill="#fff"/></svg>subscribe now</div>
    </div>
  </footer>
</div>
</body>
</html>
```